Webdesign für IT Service Firma
Zielgruppe
Wir sind eine IT-Service Firma und bieten individuelle IT-Lösungen. Unsere Kunden sind KMU, also Firmen mit einer Grösse von 2-250 Mitarbeitern im Grossraum Basel, die in Ihrem Bereich Spezialisten sind und spezielle Anforderungen an Ihre IT besitzen.
Unsere USP sind fixe Ansprechpartner, gute Erreichbarkeit, schneller und individueller Service
Aufgabenstellung
Schriftart Myriad Pro
Grün: #7FA51D
Blau: #4D9BC2
Grau: #999999
Untertitel: Wir sind da.

```html
<!DOCTYPE html>
<html lang="de">
<head>
<meta charset="utf-8">
<title>NEVALO – IT-Services aus Basel</title>
<link href="https://fonts.googleapis.com/css2?family=Roboto:wght@300;400;500;700&display=swap" rel="stylesheet">
<style>
:root{
  --green:#7FA51D;
  --green-dark:#6f9216;
  --green-pale:#e6efcf;
  --blue:#4D9BC2;
  --grey:#999999;
  --text:#333333;
  --light:#f4f4f4;
  --white:#ffffff;
}
*{box-sizing:border-box;margin:0;padding:0}
html,body{width:1200px;height:3648px;overflow:hidden}
body{font-family:"Roboto",sans-serif;color:var(--text);background:var(--white);position:relative}
.abs{position:absolute}
a{color:inherit}

/* header */
.brand{left:200px;top:18px;width:180px}
.brand-name{font-size:34px;font-weight:400;color:var(--blue);letter-spacing:1px;line-height:1;display:flex;align-items:center;gap:8px}
.brand-name i{display:inline-block;width:16px;height:16px;border-radius:50%;background:var(--green)}
.brand-tag{font-size:15px;color:var(--text);margin-top:6px}
.contact-item{top:34px;display:flex;gap:12px;align-items:flex-start;font-size:10px}
.contact-item b{display:block;color:var(--blue);font-weight:500;font-size:10px}
.contact-item span{color:var(--grey)}
.header-divider{top:28px;width:1px;height:40px;background:#e2e2e2}
.btn-appointment{left:898px;top:34px;width:128px;height:27px;border-radius:14px;background:var(--blue);color:var(--white);font-size:9px;display:flex;align-items:center;justify-content:center}

.main-nav{top:98px;left:0;width:1200px;height:40px;background:var(--green);display:flex;padding-left:172px}
.main-nav a{display:flex;align-items:center;height:40px;padding:0 16px;color:var(--white);font-size:12px;font-weight:500;text-decoration:none;border-right:1px solid rgba(255,255,255,.25)}
.main-nav a.active{background:var(--blue);padding:0 30px}
.main-nav a:last-child{border:none}

/* hero */
.hero{top:138px;left:0;width:1200px;height:420px;background:linear-gradient(180deg,#2f6f7a 0%,#4c8b7f 35%,#6a8f4a 60%,#3f8f92 80%,#2b5f5e 100%)}
.hero-title{top:268px;left:0;width:1200px;text-align:center;color:var(--white);font-size:38px;font-weight:400}
.hero-sub{top:316px;left:0;width:1200px;text-align:center;color:var(--white);font-size:14px}
.hero-btn{top:358px;left:545px;width:110px;height:28px;border-radius:14px;background:var(--green);color:var(--white);font-size:10px;display:flex;align-items:center;justify-content:center}

/* features */
.feature{top:645px;height:191px;background:var(--white);box-shadow:0 2px 12px rgba(0,0,0,.12);padding:26px 20px;font-size:8.5px;line-height:1.4}
.feature h3{display:flex;align-items:center;gap:10px;color:var(--green);font-size:15px;font-weight:400;margin-bottom:16px}
.feature p{margin-bottom:10px}
.feature.highlight{top:620px;height:252px;background:var(--green);color:var(--white);box-shadow:none;padding-top:30px}
.feature.highlight h3{color:var(--white)}
.feature-btn{display:inline-block;margin-top:8px;background:rgba(255,255,255,.18);padding:7px 10px;font-size:8.5px}

/* about */
.about-photo{left:173px;top:958px;width:323px;height:312px;background:linear-gradient(135deg,#5a5550,#9a8a70 50%,#c9c3b6)}
.about-thumb{top:1281px;width:102px;height:79px;background:linear-gradient(135deg,#d9d6cf,#a29a8c)}
.about-text{left:533px;top:963px;width:495px;font-size:8.5px;line-height:1.9}
.section-title{color:var(--green);font-size:19px;font-weight:400;margin-bottom:8px}
.sub-label{color:var(--blue);font-size:12px;margin-bottom:6px}
.about-text p{margin-bottom:10px}
.recipients{list-style:none}
.recipients li{display:flex;align-items:center;gap:6px}
.recipients a{color:var(--green)}
.btn-green{display:inline-flex;align-items:center;justify-content:center;height:29px;border-radius:15px;background:var(--green);color:var(--white);font-size:10px;padding:0 22px}

/* services */
.services{top:1454px;left:0;width:1200px;height:658px;background:radial-gradient(circle at 15% 75%,#d7e3b0 0%,#e9f0d6 40%,#f3f7e8 75%,#e6efcf 100%)}
.services-kicker{top:1516px;left:0;width:1200px;text-align:center;color:var(--blue);font-size:12px}
.services-title{top:1534px;left:0;width:1200px;text-align:center;color:var(--green);font-size:19px}
.service{width:183px;height:203px;background:var(--white);text-align:center;padding-top:14px;font-size:8px;line-height:1.4}
.service .icon{width:66px;height:66px;border-radius:50%;background:var(--green-pale);margin:0 auto 14px;display:flex;align-items:center;justify-content:center}
.service h4{font-size:12px;font-weight:500;margin-bottom:6px}
.service p{padding:0 12px;color:#555}
.service a{display:block;margin-top:12px;color:var(--green);font-weight:500}
.service.more{background:var(--green);color:var(--white);display:flex;flex-direction:column;align-items:center;justify-content:center;padding:0}
.service.more .icon{background:var(--white);margin-bottom:10px}
.service.more h4{font-size:12px}

.promo{left:307px;top:2057px;width:586px;height:103px;background:var(--white);box-shadow:0 3px 12px rgba(0,0,0,.15);border-radius:8px;overflow:hidden;display:flex}
.promo-left{width:332px;padding:20px 32px}
.promo-left h3{font-size:21px;font-weight:500;line-height:1}
.promo-left h3 span{color:var(--green)}
.promo-left p{font-size:15px;margin-top:4px}
.promo-left a{display:block;color:var(--blue);font-size:11px;margin-top:8px;text-decoration:none}
.promo-right{flex:1;background:var(--green);color:var(--white);text-align:center;font-size:9px;padding-top:18px}
.promo-right .btn-register{display:inline-block;margin-top:10px;background:var(--green-dark);padding:7px 16px;font-size:11px}

/* faq */
.faq-photo{left:173px;top:2277px;width:374px;height:250px;background:linear-gradient(135deg,#e8ecef,#9aa3ab 55%,#3e434a);box-shadow:0 3px 12px rgba(0,0,0,.2)}
.faq-text{left:598px;top:2284px;width:390px;font-size:8.5px;line-height:1.6}
.faq-kicker{color:var(--blue);font-size:12px}
.faq-list{list-style:none;margin-top:26px;width:360px}
.faq-list li{color:var(--blue);padding:8px 0;border-bottom:1px solid #ddd;display:flex;gap:8px;align-items:center}

/* news */
.news-kicker{top:2624px;left:0;width:1200px;text-align:center;color:var(--green);font-size:11px}
.news-title{top:2646px;left:0;width:1200px;text-align:center;color:var(--blue);font-size:19px;font-weight:500}
.news-card{top:2716px;width:224px;height:356px;background:#ededed;border-radius:8px;overflow:hidden}
.news-img{height:142px;position:relative}
.news-date{position:absolute;right:18px;bottom:-12px;width:38px;height:34px;background:var(--green);color:var(--white);font-size:9px;text-align:center;line-height:1.25;padding-top:5px}
.news-body{padding:20px 18px;font-size:8.5px;line-height:1.6}
.news-cat{color:var(--green);font-size:8.5px;display:flex;gap:5px;align-items:center}
.news-body h4{font-size:13px;font-weight:500;line-height:1.3;margin:10px 0 10px;color:#222}
.news-body p{color:#555}
.news-more{position:absolute;left:20px;bottom:28px;width:42px;height:26px;border-radius:13px;background:var(--green);color:var(--white);display:flex;align-items:center;justify-content:center;font-size:12px}

/* contact */
.contact-band{top:3157px;left:0;width:1200px;height:491px;background:var(--light)}
.contact-shadow{left:240px;top:3243px;width:223px;height:338px;background:var(--blue)}
.contact-box{left:230px;top:3233px;width:221px;height:338px;background:var(--green);color:var(--white);padding:0 18px}
.contact-row{display:flex;gap:12px;padding:28px 0 18px;border-bottom:1px dashed rgba(255,255,255,.55)}
.contact-row:last-child{border:none}
.contact-row h4{font-size:16px;font-weight:500}
.contact-row p{font-size:9.5px;line-height:1.6}
.contact-form{left:509px;top:3250px;width:412px}
.contact-form .kicker{color:var(--blue);font-size:11px}
.contact-form h3{color:var(--green);font-size:15px;font-weight:500;margin-top:6px}
.field{font-size:10px;border-bottom:1px solid #bbb;padding-bottom:10px;margin-top:28px}
.field-row{display:flex;gap:38px}
.field-row .field{flex:1}
.field.message{height:100px}
.btn-send{display:inline-flex;gap:10px;margin-top:26px;height:29px;border-radius:15px;background:var(--green);color:var(--white);font-size:10px;align-items:center;padding:0 18px}
</style>
</head>
<body>

<header>
  <div class="abs brand">
    <div class="brand-name"><i></i>NEVALO</div>
    <div class="brand-tag">IT-Services aus Basel</div>
  </div>
  <div class="abs contact-item" style="left:570px">
    <svg width="20" height="16" viewBox="0 0 20 16"><rect x="1" y="1" width="18" height="14" fill="none" stroke="#7FA51D" stroke-width="1.4"/><path d="M1 1l9 8 9-8" fill="none" stroke="#7FA51D" stroke-width="1.4"/></svg>
    <div><b>Mailen Sie uns</b><span>support@nevalo.ch</span></div>
  </div>
  <div class="abs header-divider" style="left:710px"></div>
  <div class="abs contact-item" style="left:736px">
    <svg width="20" height="18" viewBox="0 0 24 24"><path d="M6 2l4 5-2 3c1 3 3 5 6 6l3-2 5 4-3 4C10 22 2 14 2 5z" fill="none" stroke="#7FA51D" stroke-width="1.4"/></svg>
    <div><b>Rufen Sie uns an</b><span>+41 61 000 4821</span></div>
  </div>
  <div class="abs header-divider" style="left:870px"></div>
  <div class="abs btn-appointment">Einen Termin machen</div>
</header>

<nav class="abs main-nav">
  <a class="active">HOME</a><a>LEISTUNGEN</a><a>PRIVATKUNDE?</a><a>JOBS</a><a>HILFE</a><a>SOZIALPROZENT</a><a>ÜBER UNS</a><a>KONTAKT</a>
</nav>

<section class="abs hero" role="img" aria-label="Stadtansicht von Basel am Rhein mit Altstadt und Münster"></section>
<h1 class="abs hero-title">WIR KÜMMERN UNS UM IHRE IT</h1>
<p class="abs hero-sub">DAMIT SIE SICH AUF IHR KERNGESCHÄFT KONZENTRIEREN KÖNNEN.</p>
<div class="abs hero-btn">WEITERLESEN</div>

<article class="abs feature" style="left:227px;width:238px">
  <h3><svg width="36" height="34" viewBox="0 0 36 34" fill="none" stroke="#7FA51D" stroke-width="1.4"><circle cx="14" cy="16" r="6"/><path d="M6 16a8 8 0 0116 0M4 32c0-6 5-9 10-9s10 3 10 9"/><rect x="22" y="2" width="12" height="8" rx="2"/></svg>SUPPORT</h3>
  <p>Sie benötigen eine stabile IT, damit Sie sich voll auf Ihr Kerngeschäft konzentrieren können?</p>
  <p>Sie brauchen einen verlässlichen IT-Dienstleister, der Sie auch in Notfällen nicht im Stich lässt?</p>
  <p>Vertrauen Sie uns, wir kümmern uns um Sie!</p>
</article>
<article class="abs feature highlight" style="left:465px;width:242px">
  <h3><svg width="38" height="40" viewBox="0 0 38 40" fill="none" stroke="#fff" stroke-width="1.6"><path d="M19 2l15 6v12c0 9-7 16-15 18C11 36 4 29 4 20V8z"/><path d="M12 20l5 5 9-10"/></svg>SICHERHEIT</h3>
  <p>Die Daten Ihrer Unternehmung sind die Basis und das Kapital Ihres Geschäfts.</p>
  <p>Ein Verlust oder eine Weitergabe an Dritte bedeutet erhebliche Verluste oder kann gar zur Beendigung Ihres Unternehmens führen.</p>
  <p>Vertrauen Sie uns, wir kümmern uns um Sie!</p>
  <span class="feature-btn">KONTAKTIEREN SIE UNS JETZT</span>
</article>
<article class="abs feature" style="left:707px;width:244px">
  <h3><svg width="44" height="36" viewBox="0 0 44 36" fill="none" stroke="#7FA51D" stroke-width="1.4"><rect x="2" y="2" width="16" height="10"/><rect x="24" y="2" width="18" height="10"/><circle cx="10" cy="22" r="4"/><circle cx="32" cy="22" r="4"/><path d="M2 34c0-4 4-6 8-6s8 2 8 6M24 34c0-4 4-6 8-6s8 2 8 6"/></svg>BERATUNG</h3>
  <p>Ihre IT-Prozesse und Systeme verlangsamen Ihren Arbeitsfluss, anstatt Sie produktiver zu machen?</p>
  <p>Gerne analysieren wir Ihre Infrastruktur und Systeme und helfen Ihnen dabei Effizienzgewinne zu realisieren.</p>
  <p>Vertrauen Sie uns, wir kümmern uns um Sie!</p>
</article>

<div class="abs about-photo" role="img" aria-label="Foto: Team-Meeting in einem Konferenzraum mit Laptops"></div>
<div class="abs about-thumb" style="left:173px" role="img" aria-label="Foto: Büroraum mit Tischen"></div>
<div class="abs about-thumb" style="left:283px" role="img" aria-label="Foto: Arbeitsplatz am Fenster"></div>
<div class="abs about-thumb" style="left:393px" role="img" aria-label="Foto: Büro mit Schreibtisch"></div>

<section class="abs about-text">
  <h2 class="section-title">ÜBER UNS</h2>
  <p>2012 gegründet durch die Partner Marco Brandli und Lukas Ammann als Weiterentwicklung diverser gemeinsamer Projekte, ist die NEVALO GmbH ein Partner für IT Dienstleistungen. Unser Ziel ist dabei stets eine massgeschneiderte Lösung für unsere Kunden zu finden. Unsere Leitgedanken sind dabei der Kundenfokus, die Einfachheit, sowie Robustheit der Lösung. Wir entwickeln Lösungen aufgrund Ihrer Bedürfnisse und Geschäftsprozesse. Die Qualität unseres Angebots basiert auf der Verknüpfung von aktuellen IT Lösungen und dem Verständnis, was sie als Firma ausmacht.</p>
  <h2 class="section-title" style="margin-top:14px">UNSER ENGAGEMENT</h2>
  <div class="sub-label">SOZIALPROZENT</div>
  <p>Mit unserem Sozialprozent - ein Prozent unseres Umsatzes spenden wir jedes Jahr für wohltätige Zwecke - nehmen wir unsere soziale Verantwortung war.</p>
  <p style="font-size:10px;margin-bottom:4px">Empfänger der letzten Jahre waren:</p>
  <ul class="recipients">
    <li><svg width="10" height="8" viewBox="0 0 10 8"><path d="M1 4l3 3 5-6" fill="none" stroke="#7FA51D" stroke-width="1.6"/></svg>Bergrettung Nordwest, <a>www.bergrettung-nw.ch</a></li>
    <li><svg width="10" height="8" viewBox="0 0 10 8"><path d="M1 4l3 3 5-6" fill="none" stroke="#7FA51D" stroke-width="1.6"/></svg>Jugendraum Rhein, <a>www.jugendraum-rhein.ch</a></li>
    <li><svg width="10" height="8" viewBox="0 0 10 8"><path d="M1 4l3 3 5-6" fill="none" stroke="#7FA51D" stroke-width="1.6"/></svg>Hilfe ohne Grenzen, <a>www.hilfe-og.ch</a></li>
    <li><svg width="10" height="8" viewBox="0 0 10 8"><path d="M1 4l3 3 5-6" fill="none" stroke="#7FA51D" stroke-width="1.6"/></svg>Tierhilfe Regio, <a>www.tierhilfe-regio.ch</a></li>
  </ul>
  <div class="btn-green" style="margin-top:24px">WEITERLESEN</div>
</section>

<section class="abs services"></section>
<p class="abs services-kicker">WAS WIR ANBIETEN</p>
<h2 class="abs services-title">WIR FINDEN LÖSUNGEN FÜR JEDES PROBLEM</h2>

<article class="abs service" style="left:218px;top:1594px"><div class="icon"><svg width="36" height="30" viewBox="0 0 36 30" fill="none" stroke="#7FA51D" stroke-width="1.4"><rect x="2" y="8" width="24" height="16"/><path d="M0 27h30"/><circle cx="28" cy="8" r="6"/></svg></div><h4>IT-BETREUUNG</h4><p>Wir bieten mehr als Hardware und Software: Wir bieten IT als massgeschneiderte Dienstleistung.</p><a>Weiterlesen</a></article>
<article class="abs service" style="left:412px;top:1594px"><div class="icon"><svg width="28" height="32" viewBox="0 0 28 32" fill="none" stroke="#7FA51D" stroke-width="1.4"><path d="M14 2l11 5v9c0 7-5 12-11 14C8 28 3 23 3 16V7z"/><rect x="9" y="14" width="10" height="8"/><path d="M11 14v-3a3 3 0 016 0v3"/></svg></div><h4>IT SICHERHEIT</h4><p>Wir bieten mehr als Hardware und Software: Wir bieten IT als massgeschneiderte Dienstleistung.</p><a>Weiterlesen</a></article>
<article class="abs service" style="left:605px;top:1594px"><div class="icon"><svg width="34" height="30" viewBox="0 0 34 30" fill="none" stroke="#7FA51D" stroke-width="1.4"><rect x="2" y="2" width="30" height="8"/><rect x="2" y="12" width="30" height="8"/><rect x="2" y="22" width="30" height="6"/><path d="M6 6h4M6 16h4"/></svg></div><h4>BACKUPLÖSUNGEN</h4><p>Wir bieten mehr als Hardware und Software: Wir bieten IT als massgeschneiderte Dienstleistung.</p><a>Weiterlesen</a></article>
<article class="abs service" style="left:799px;top:1594px"><div class="icon"><svg width="34" height="30" viewBox="0 0 34 30" fill="none" stroke="#7FA51D" stroke-width="1.4"><rect x="2" y="2" width="30" height="20"/><path d="M8 16l5-6 5 4 6-8M12 28h10M17 22v6"/></svg></div><h4>SCIENTIFIC COMPUTING</h4><p>Wir bieten mehr als Hardware und Software: Wir bieten IT als massgeschneiderte Dienstleistung.</p><a>Weiterlesen</a></article>

<article class="abs service" style="left:218px;top:1807px"><div class="icon"><svg width="34" height="34" viewBox="0 0 34 34" fill="none" stroke="#7FA51D" stroke-width="1.4"><circle cx="17" cy="17" r="15"/><ellipse cx="17" cy="17" rx="7" ry="15"/><path d="M2 17h30"/></svg></div><h4>WEB ENTWICKLUNG</h4><p>Wir bieten mehr als Hardware und Software: Wir bieten IT als massgeschneiderte Dienstleistung.</p><a>Weiterlesen</a></article>
<article class="abs service" style="left:412px;top:1807px"><div class="icon"><svg width="34" height="30" viewBox="0 0 34 30" fill="none" stroke="#7FA51D" stroke-width="1.4"><rect x="2" y="2" width="30" height="20"/><rect x="6" y="6" width="10" height="8"/><path d="M20 8h8M20 12h8M12 28h10"/></svg></div><h4>HOTELBUCHUNG</h4><p>Wir bieten mehr als Hardware und Software: Wir bieten IT als massgeschneiderte Dienstleistung.</p><a>Weiterlesen</a></article>
<article class="abs service" style="left:605px;top:1807px"><div class="icon"><svg width="34" height="34" viewBox="0 0 34 34" fill="none" stroke="#7FA51D" stroke-width="1.4"><circle cx="17" cy="17" r="6"/><circle cx="6" cy="6" r="4"/><circle cx="28" cy="6" r="4"/><circle cx="6" cy="28" r="4"/><circle cx="28" cy="28" r="4"/><path d="M9 9l4 4M25 9l-4 4M9 25l4-4M25 25l-4-4"/></svg></div><h4>COWORKING-SPACE</h4><p>Wir bieten mehr als Hardware und Software: Wir bieten IT als massgeschneiderte Dienstleistung.</p><a>Weiterlesen</a></article>
<article class="abs service more" style="left:799px;top:1807px"><div class="icon"><svg width="30" height="30" viewBox="0 0 30 30" fill="none" stroke="#7FA51D" stroke-width="2"><rect x="3" y="3" width="10" height="10" rx="2"/><rect x="17" y="3" width="10" height="10" rx="2"/><rect x="3" y="17" width="10" height="10" rx="2"/><rect x="17" y="17" width="10" height="10" rx="2"/></svg></div><h4>MEHR<br>DIENSTLEISTUNGEN</h4></article>

<aside class="abs promo">
  <div class="promo-left">
    <h3><span>AKTION:</span> 50% RABATT AUF</h3>
    <p>DIE ERSTEN 10 MINUTEN!</p>
    <a>support@nevalo.ch</a>
  </div>
  <div class="promo-right">
    Unsere Leistungen werden pro angefangene<br>10 Minuten mit 19,00 CHF inkl. 7,7% MwSt.<br>
    <span class="btn-register">Jetzt registrieren</span>
  </div>
</aside>

<div class="abs faq-photo" role="img" aria-label="Foto: Geschäftsleute im Gespräch an einem Konferenztisch"></div>
<section class="abs faq-text">
  <p class="faq-kicker">OFT GESTELLTE FRAGE</p>
  <h2 class="section-title">FRAGE STELLEN MEHR</h2>
  <p>Lorem ipsum dolor sit amet, consectetur adipiscing elit. Ut elit tellus, luctus nec ullamcorper mattis, pulvinar dapibus leo.Lorem ipsum dolor sit amet, consectetur adipiscing elit. Ut elit tellus, luctus nec ullamcorper mattis, pulvinar dapibus leo.</p>
  <ul class="faq-list">
    <li><svg width="5" height="8" viewBox="0 0 5 8"><path d="M0 0l5 4-5 4z" fill="#4D9BC2"/></svg>Wie bestelle ich den Service?</li>
    <li><svg width="5" height="8" viewBox="0 0 5 8"><path d="M0 0l5 4-5 4z" fill="#4D9BC2"/></svg>Kann ich ein Angebot machen?</li>
    <li><svg width="5" height="8" viewBox="0 0 5 8"><path d="M0 0l5 4-5 4z" fill="#4D9BC2"/></svg>Wie lange Garantie?</li>
  </ul>
</section>

<p class="abs news-kicker">BLEIBEN SIE MIT NEVALO AUF DEM LAUFENDEN</p>
<h2 class="abs news-title">VON DEN NEUESTEN &amp; BELIEBTEN NEWS</h2>

<article class="abs news-card" style="left:242px">
  <div class="news-img" role="img" aria-label="Foto: Nahaufnahme eines Industrieobjektivs" style="background:linear-gradient(135deg,#3a3a3a,#8a8a8a 50%,#2a2a2a)"><div class="news-date">July 19<br>2021</div></div>
  <div class="news-body"><div class="news-cat"><svg width="10" height="8" viewBox="0 0 10 8"><path d="M.5 1h3l1 1h5v5.5h-9z" fill="none" stroke="#7FA51D"/></svg>Artificial Store</div>
  <h4>Repeated of endeavor mr position kindness.</h4><p>Lorem ipsum dolor sit amet, consectetur adipiscing elit, sed do eiusmod tempor incididunt ut labore.</p></div>
  <div class="news-more">→</div>
</article>
<article class="abs news-card" style="left:486px">
  <div class="news-img" role="img" aria-label="Foto: Zwei Personen in einer Werkstatt mit Maschine" style="background:linear-gradient(135deg,#c9d3dc,#7d8fa3 50%,#3c5f8a)"><div class="news-date">July 19<br>2021</div></div>
  <div class="news-body"><div class="news-cat"><svg width="10" height="8" viewBox="0 0 10 8"><path d="M.5 1h3l1 1h5v5.5h-9z" fill="none" stroke="#7FA51D"/></svg>Automation</div>
  <h4>Justifying Automation in Your Factory.</h4><p>Lorem ipsum dolor sit amet, consectetur adipiscing elit, sed do eiusmod tempor incididunt ut labore.</p></div>
  <div class="news-more">→</div>
</article>
<article class="abs news-card" style="left:731px">
  <div class="news-img" role="img" aria-label="Foto: Industrieroboter in einer Küche" style="background:linear-gradient(135deg,#dcdcdc,#9a9a9a 50%,#5a5a5a)"><div class="news-date">July 19<br>2021</div></div>
  <div class="news-body"><div class="news-cat"><svg width="10" height="8" viewBox="0 0 10 8"><path d="M.5 1h3l1 1h5v5.5h-9z" fill="none" stroke="#7FA51D"/></svg>Digitalization</div>
  <h4>Boost Your Cobot Safety Know-How with These Digital Resources</h4><p>Lorem ipsum dolor sit amet, consectetur adipiscing elit, sed do eiusmod tempor incididunt ut labore.</p></div>
  <div class="news-more">→</div>
</article>

<section class="abs contact-band"></section>
<div class="abs contact-shadow"></div>
<div class="abs contact-box">
  <div class="contact-row">
    <svg width="26" height="24" viewBox="0 0 26 24"><path d="M1 6l7-3 8 3 8-3v16l-8 3-8-3-7 3z" fill="#fff"/><circle cx="17" cy="8" r="3" fill="#7FA51D"/></svg>
    <div><h4>NEVALO GmbH</h4><p>Lindenweg 14 -<br>CH-4052 Basel</p></div>
  </div>
  <div class="contact-row">
    <svg width="26" height="24" viewBox="0 0 24 24"><path d="M6 2l4 5-2 3c1 3 3 5 6 6l3-2 5 4-3 4C10 22 2 14 2 5z" fill="#fff"/></svg>
    <div><h4>Einen Anruf tätigen</h4><p>+41 61 000 4821</p></div>
  </div>
  <div class="contact-row">
    <svg width="26" height="24" viewBox="0 0 26 24"><path d="M2 9l11-7 11 7v13H2z" fill="#fff"/><path d="M2 9l11 7 11-7" fill="none" stroke="#7FA51D" stroke-width="1.4"/></svg>
    <div><h4>Senden Sie eine E-Mail</h4><p>support@nevalo.ch</p></div>
  </div>
</div>

<form class="abs contact-form">
  <p class="kicker">WIR FREUEN UNS JEDERZEIT VON IHNEN ZU HÖREN</p>
  <h3>MACHEN SIE SICH BEREIT, IHR PROJEKT MIT UNS ZU STARTEN</h3>
  <div class="field">Name</div>
  <div class="field-row"><div class="field">Email*</div><div class="field">Phone</div></div>
  <div class="field message">Tell Us About Project*</div>
  <div class="btn-send">NACHRICHT SENDEN <svg width="14" height="12" viewBox="0 0 14 12"><path d="M0 5L14 0 10 12 7 7z" fill="#fff"/></svg></div>
</form>

</body>
</html>
```